A UK based Lettings and Property Management Company - Brindle Oak Property

Brindle Oak Property rents and manages properties on behalf of owners in Liverpool, UK. We are looking for a clean, fresh modern design which incororates our logo.

In terms of pages we initially require:

Home
Lettings
Property Management
Landlords
Tenants
About
Contact

In would like to use colours compatible with the logo

Target Market(s)

People looking to rent property
Owners looking to use our services to let their property

Industry/Entity Type

Property

Contact Information for Business Card

Logo prominent on one side
Address to be edited by us as we are moving premises in October
Name Gareth Whitlow
Tel number 0151 486 2037
e-mail gareth@brindleoakhomes.co.uk

Font styles to use
Sans Serif

Colors

Designer to choose colors to be used in the design.

Requirements
Must have
• Clean lines
• Fresh
• Easy navigation
• Easy editing
• Data capture

```html
<!DOCTYPE html>
<html lang="en">
<head>
<meta charset="utf-8">
<title>Brindle Oak Property</title>
<link href="https://fonts.googleapis.com/css2?family=Mulish:wght@400;600;700;800&display=swap" rel="stylesheet">
<style>
:root{
  --navy:#17173a;
  --blue:#4a80d6;
  --dark:#333335;
  --beige:#eee5d5;
  --grey:#efefef;
  --field:#ececec;
  --text:#444;
  --muted:#888;
  --green:#3d9b3d;
  --white:#fff;
}
*{box-sizing:border-box;margin:0;padding:0}
html,body{width:1200px;height:3051px;overflow:hidden}
body{position:relative;background:var(--white);font-family:"Mulish",sans-serif;color:var(--text)}
.abs{position:absolute}
.top-band{left:0;top:0;width:1200px;height:588px;background:var(--grey)}
.brand{left:102px;top:24px;display:flex;align-items:center;gap:10px}
.brand-mark{width:48px;height:48px;background:var(--navy)}
.brand-name{font-weight:800;font-size:21px;line-height:22px;color:var(--navy);letter-spacing:1px;text-transform:uppercase}
.call{right:102px;top:24px;font-size:15px;color:var(--dark);font-weight:600;display:flex;align-items:center;gap:6px}
.call b{color:var(--blue)}
.nav{right:102px;top:58px;display:flex;gap:32px;font-size:13px;color:var(--dark)}
.nav .active{color:var(--blue)}
.hero{left:102px;top:100px;width:996px;height:488px;background:linear-gradient(180deg,#4a4660 0%,#5b5468 45%,#3b3530 100%)}
.hero-inner{left:0;top:0;width:100%;text-align:center;padding-top:170px;color:var(--white)}
.hero h1{font-size:42px;font-weight:700;letter-spacing:1px}
.hero p{font-size:18px;margin-top:6px;letter-spacing:1px}
.btn-blue{display:inline-block;background:var(--blue);color:var(--white);font-size:13px;padding:10px 22px;margin-top:34px}
.hero-arrow{width:24px;height:34px;top:228px;display:flex;align-items:center;justify-content:center}
.hero-arrow.l{left:-12px;background:var(--white)}
.hero-arrow.r{right:-12px;background:var(--blue)}
.intro{left:0;top:652px;width:1200px;text-align:center}
.intro-mark{width:54px;height:54px;background:var(--navy);margin:0 auto}
.intro h2{font-size:25px;color:var(--navy);margin-top:16px;font-weight:700}
.intro h2 span{color:var(--blue)}
.intro p{width:620px;margin:12px auto 0;font-size:13.5px;line-height:19px;color:var(--text)}
.btn-outline{display:inline-block;border:2px solid #b8c9e8;font-size:13px;padding:7px 14px;margin-top:26px;color:var(--dark)}
.section-title{left:0;width:1200px;text-align:center;font-size:25px;font-weight:700;color:var(--navy)}
.beige{left:0;top:1032px;width:1200px;height:366px;background:var(--beige)}
.service{top:1032px;width:314px;height:366px;background:var(--dark);color:var(--white);text-align:center}
.service h3{height:58px;line-height:58px;font-size:16px;font-weight:600}
.service .photo{height:170px}
.service p{font-size:12px;line-height:17px;padding:14px 30px 0}
.service.featured{top:1022px;height:383px;background:var(--blue)}
.service.featured h3{height:68px;line-height:68px}
.circle-btn{width:52px;height:52px;border-radius:50%;background:var(--blue);color:var(--white);font-size:13px;font-weight:700;display:flex;align-items:center;justify-content:center;left:131px;bottom:-26px}
.service.featured .circle-btn{background:var(--navy);bottom:-30px}
.listing{top:1555px;width:298px;height:342px;background:var(--field)}
.listing .photo{height:170px;position:relative}
.tag{position:absolute;left:0;bottom:-10px;background:var(--green);color:var(--white);font-size:10px;font-weight:700;padding:4px 10px}
.listing .body{padding:18px 26px 0}
.listing .type{font-size:11px;color:var(--dark)}
.listing h4{font-size:16px;color:var(--navy);margin-top:8px;font-weight:700}
.listing .loc{font-size:12px;color:#666}
.listing .price{font-size:17px;color:var(--blue);font-weight:700;margin-top:16px;padding-bottom:12px;border-bottom:1px solid #d6d6d6}
.listing .spec{font-size:11px;color:#555;margin-top:14px}
.testimonial{top:2018px;width:420px}
.avatar{width:160px;height:160px;border-radius:50%;border:2px solid #ddd;padding:10px;margin-left:0}
.avatar div{width:100%;height:100%;border-radius:50%}
.testimonial .name{font-size:14px;color:var(--dark);margin-top:-4px}
.testimonial .name span{color:var(--muted)}
.testimonial p{font-size:13px;line-height:20px;margin-top:12px;width:370px}
.stars{margin-top:14px;display:flex;gap:4px}
.contact-band{left:0;top:2358px;width:1200px;height:307px;background:var(--grey)}
.form-box{left:126px;top:2430px;width:541px;height:470px;background:var(--white);box-shadow:0 6px 24px rgba(0,0,0,.12)}
.form-strip{left:126px;top:2543px;width:24px;height:357px;background:var(--blue)}
.form-box h3{position:absolute;left:80px;top:64px;font-size:25px;font-weight:600;color:var(--navy)}
.form-box .rule{position:absolute;left:80px;top:114px;width:140px;height:2px;background:#ccc}
.field{position:absolute;left:80px;width:404px;height:34px;background:var(--field);font-size:12px;color:var(--muted);padding:10px 16px}
.send{left:550px;top:2818px;width:36px;height:36px;border-radius:50%;background:var(--blue);display:flex;align-items:center;justify-content:center}
.info-box{left:667px;top:2430px;width:405px;height:470px;background:var(--dark);color:var(--white);padding:66px 50px}
.info-box h3{font-size:20px;font-weight:600}
.info-box .addr{font-size:14px;line-height:21px;margin-top:42px}
.info-box .lbl{font-size:14px;margin-top:22px}
.info-box .phone{font-size:19px;margin-top:4px}
.info-box .mail{font-size:15px;margin-top:4px;text-decoration:underline}
.socials{display:flex;gap:10px;margin-top:42px}
.socials span{width:36px;height:36px;border-radius:50%;border:1px solid #888}
.socials span.on{background:var(--blue);border-color:var(--blue)}
.footer{left:180px;top:2966px;font-size:14px;color:#555}
.to-top{left:1000px;top:2962px}
</style>
</head>
<body>
<div class="abs top-band"></div>

<header>
  <div class="abs brand"><div class="brand-mark"></div><div class="brand-name">Brindle Oak<br>Property</div></div>
  <div class="abs call"><b>Call Us:</b>
    <svg width="12" height="14" viewBox="0 0 12 14"><path d="M3 1l2 3-1.5 1.5c.8 2 2 3.2 4 4L9 8l3 2-1 3C6 13 0 8 1 2z" fill="#4a80d6"/></svg>
    0151 486 2037</div>
  <nav class="abs nav">
    <span class="active">Home</span><span>About Us</span><span>Lettings</span><span>Property Management</span><span>Landlords</span><span>Tenants</span><span>Contact</span>
  </nav>
</header>

<section class="abs hero" role="img" aria-label="Modern two-storey house photographed at dusk">
  <div class="abs hero-inner">
    <h1>Brindle Oak Property</h1>
    <p>Rents and Manages Properties</p>
    <span class="btn-blue">Contact Us »</span>
  </div>
  <div class="abs hero-arrow l"><svg width="14" height="8"><path d="M14 4H2M5 1L2 4l3 3" stroke="#333" fill="none" stroke-width="1.5"/></svg></div>
  <div class="abs hero-arrow r"><svg width="14" height="8"><path d="M0 4h12M9 1l3 3-3 3" stroke="#fff" fill="none" stroke-width="1.5"/></svg></div>
</section>

<section class="abs intro">
  <div class="intro-mark"></div>
  <h2>Brindle Oak <span>Property</span></h2>
  <p>There are many variations of passages of Lorem Ipsum available, but the majority have suffered alteration in some form, by injected humour, or randomised words which don't look even slightly believable. If you are going to use a passage of Lorem Ipsum, you need to be sure there isn't anything embarrassing...</p>
  <span class="btn-outline">Discover More »</span>
</section>

<h2 class="abs section-title" style="top:962px">What We Do</h2>
<div class="abs beige"></div>
<article class="abs service" style="left:128px">
  <h3>Lettings</h3>
  <div class="photo" role="img" aria-label="House keys with a small house keyring on a wooden table" style="background:linear-gradient(135deg,#c99a62,#8a5a2e)"></div>
  <p>It is a long established fact that a reader will be distracted by the readable content of a page when looking more-or-less normal...</p>
  <div class="abs circle-btn">More</div>
</article>
<article class="abs service featured" style="left:443px">
  <h3>Property Management</h3>
  <div class="photo" role="img" aria-label="Two people shaking hands over documents" style="background:linear-gradient(135deg,#dfe3ea,#9aa3b3)"></div>
  <p>It is a long established fact that a reader will be distracted by the readable content of a page when looking more-or-less normal...</p>
  <div class="abs circle-btn"><svg width="14" height="10"><path d="M0 5h12M8 1l4 4-4 4" stroke="#fff" fill="none" stroke-width="2"/></svg></div>
</article>
<article class="abs service" style="left:758px">
  <h3>Landlords</h3>
  <div class="photo" role="img" aria-label="Hands sheltering a small model house" style="background:linear-gradient(135deg,#f3ede6,#c9b7a3)"></div>
  <p>It is a long established fact that a reader will be distracted by the readable content of a page when looking more-or-less normal...</p>
  <div class="abs circle-btn">More</div>
</article>

<h2 class="abs section-title" style="top:1494px">Property Listings</h2>
<svg class="abs" style="left:66px;top:1712px" width="36" height="26"><path d="M34 13H3M14 2L3 13l11 11" stroke="#aaa" fill="none" stroke-width="2"/></svg>
<svg class="abs" style="left:1098px;top:1712px" width="36" height="26"><path d="M2 13h31M22 2l11 11-11 11" stroke="#4a80d6" fill="none" stroke-width="2"/></svg>
<article class="abs listing" style="left:127px">
  <div class="photo" role="img" aria-label="White villa with a pool at dusk" style="background:linear-gradient(180deg,#6f9bd1,#c9c4b5)"><span class="tag">RENT</span></div>
  <div class="body"><div class="type">House</div><h4>Lifestyle or Holiday Home</h4><div class="loc">(Kelsall UK 2076 )</div><div class="price">Price: $10,000.00</div><div class="spec">2500Sq ft &nbsp;/ &nbsp;4 Bedroom &nbsp;/ &nbsp;3 Bath</div></div>
</article>
<article class="abs listing" style="left:450px">
  <div class="photo" role="img" aria-label="Modern apartment building under a blue sky" style="background:linear-gradient(180deg,#2f78c4,#8aa6b8)"><span class="tag">RENT</span></div>
  <div class="body"><div class="type">Villa</div><h4>Freedom, Space &amp; Solitude</h4><div class="loc">(Kelsall UK 2076 )</div><div class="price">Price: $10,000.00</div><div class="spec">2500Sq ft &nbsp;/ &nbsp;4 Bedroom &nbsp;/ &nbsp;3 Bath</div></div>
</article>
<article class="abs listing" style="left:774px">
  <div class="photo" role="img" aria-label="Large family house lit up at twilight" style="background:linear-gradient(180deg,#8e86c9,#4f5a3f)"><span class="tag">RENT</span></div>
  <div class="body"><div class="type">Family Home</div><h4>Lifestyle or Holiday Home</h4><div class="loc">(Kelsall UK 2076 )</div><div class="price">Price: $50,000.00</div><div class="spec">2500Sq ft &nbsp;/ &nbsp;4 Bedroom &nbsp;/ &nbsp;3 Bath</div></div>
</article>

<h2 class="abs section-title" style="top:1954px">Testimonials</h2>
<svg class="abs" style="left:126px;top:2154px" width="24" height="44"><path d="M22 2L3 22l19 20" stroke="#aaa" fill="none" stroke-width="2"/></svg>
<svg class="abs" style="left:1048px;top:2154px" width="24" height="44"><path d="M2 2l19 20L2 42" stroke="#4a80d6" fill="none" stroke-width="2"/></svg>
<article class="abs testimonial" style="left:208px">
  <div class="avatar"><div role="img" aria-label="Portrait of a smiling client" style="background:linear-gradient(135deg,#8fa7c4,#4a5a72)"></div></div>
  <div class="name">Marla T. <span>/ Distribution</span></div>
  <p>Contrary to popular belief, Lorem Ipsum is not simply random text. It has roots in a piece of classical Latin literature from 45 BC, making it over...</p>
  <div class="stars"><svg width="100" height="14"><g fill="#3d9b3d"><path id="st" d="M7 0l2 4.5 5 .5-3.8 3.3L11.4 13 7 10.5 2.6 13l1.2-4.7L0 5l5-.5z"/><use href="#st" x="16"/><use href="#st" x="32"/></g><path d="M55 0l2 4.5 5 .5-3.8 3.3 1.2 4.7L55 10.5V0z" fill="#3d9b3d"/><path d="M55 0l2 4.5 5 .5-3.8 3.3 1.2 4.7L55 10.5 50.6 13l1.2-4.7L48 5l5-.5z" fill="none" stroke="#3d9b3d"/><path d="M71 1l2 4 4.5.5-3.4 3 1 4.3L71 10.5 67 12.8l1-4.3-3.4-3 4.5-.5z" fill="none" stroke="#3d9b3d"/></svg></div>
</article>
<article class="abs testimonial" style="left:668px">
  <div class="avatar"><div role="img" aria-label="Portrait of a smiling client" style="background:linear-gradient(135deg,#e6ddd4,#a08570)"></div></div>
  <div class="name">Rowena H. <span>/ Distribution</span></div>
  <p>Contrary to popular belief, Lorem Ipsum is not simply random text. It has roots in a piece of classical Latin literature from 45 BC, making it over...</p>
  <div class="stars"><svg width="100" height="14"><g fill="#3d9b3d"><path id="st2" d="M7 0l2 4.5 5 .5-3.8 3.3L11.4 13 7 10.5 2.6 13l1.2-4.7L0 5l5-.5z"/><use href="#st2" x="16"/><use href="#st2" x="32"/></g><path d="M55 0l2 4.5 5 .5-3.8 3.3 1.2 4.7L55 10.5V0z" fill="#3d9b3d"/><path d="M55 0l2 4.5 5 .5-3.8 3.3 1.2 4.7L55 10.5 50.6 13l1.2-4.7L48 5l5-.5z" fill="none" stroke="#3d9b3d"/><path d="M71 1l2 4 4.5.5-3.4 3 1 4.3L71 10.5 67 12.8l1-4.3-3.4-3 4.5-.5z" fill="none" stroke="#3d9b3d"/></svg></div>
</article>

<div class="abs contact-band"></div>
<section class="abs form-box">
  <h3>Send us a Message</h3>
  <div class="rule"></div>
  <div class="field" style="top:148px">Your Name</div>
  <div class="field" style="top:196px">Enter your Email</div>
  <div class="field" style="top:244px">Phone</div>
  <div class="field" style="top:292px;height:102px">Type your Message</div>
</section>
<div class="abs form-strip"></div>
<div class="abs send"><svg width="16" height="14"><path d="M0 6L16 0 12 14 7 9z" fill="#fff"/></svg></div>
<section class="abs info-box">
  <h3>Contact Info</h3>
  <div class="addr">Brindle Oak Property<br>48 Canning Row,<br>Liverpool, L1 7QX</div>
  <div class="lbl">Phone:</div>
  <div class="phone">0151 486 2037</div>
  <div class="lbl">Email:</div>
  <div class="mail">info@brindleoakproperty.co.uk</div>
  <div class="socials"><span class="on"></span><span></span><span></span></div>
</section>

<footer>
  <div class="abs footer">2017 © Brindle Oak Property All rights reserved.</div>
  <svg class="abs to-top" width="14" height="16"><path d="M7 15V2M2 7l5-5 5 5" stroke="#4a80d6" fill="none" stroke-width="2"/></svg>
</footer>
</body>
</html>
```